Business Card Design Project

We require a professional business card designed for our consulting organisation that has the same theme and colours as our logo except for the grey.

Colours on the front should predominately be white however some reference to our logo colours except for the grey.

The back of the card should be have background colour that aligns with our logo colour.

Layout, style and design is up to the designer. So send through your designs

Details are attached in the word document project brief.

Target Market(s)

Target market are large corporate organisations

Industry/Entity Type

Business

Requirements
Must have
• Content on the front must have:

Dale Fenwick
Managing Director

P: 0412 557 208
E: Dale@braviotraxgroup.com
W: www.braviotraxgroup.com

Content on the back must have the words:
Alliances
Placement
Training
Support

Design Colours
Must align to our logo

```html
<!DOCTYPE html>
<html lang="en">
<head>
<meta charset="utf-8">
<title>Braviotrax Group – Business Card</title>
<link rel="stylesheet" href="https://fonts.googleapis.com/css2?family=Open+Sans:wght@400;600;700&display=swap">
<style>
  :root {
    --brand-blue: #1d6fb8;
    --brand-blue-dark: #175e9e;
    --card-white: #ffffff;
    --text-grey: #5a5f66;
    --divider: #d3d7dc;
    --backdrop: #eceef1;
  }
  * { box-sizing: border-box; margin: 0; padding: 0; }
  html, body {
    width: 1200px; height: 720px; overflow: hidden;
    background: var(--backdrop);
    font-family: "Open Sans", Arial, sans-serif;
  }
  .stage {
    position: relative; width: 1200px; height: 720px;
    display: flex; align-items: center; justify-content: center; gap: 40px;
  }
  .card {
    position: relative; width: 540px; height: 310px; overflow: hidden;
    box-shadow: 0 6px 18px rgba(0,0,0,0.12);
  }

  /* Front */
  .card--front { background: var(--card-white); }
  .front-band { position: absolute; inset: 0; width: 100%; height: 100%; }
  .front-brand {
    position: absolute; left: 40px; top: 92px;
    display: flex; align-items: center; gap: 12px;
  }
  .front-brand__mark {
    width: 34px; height: 34px; background: var(--brand-blue);
  }
  .front-brand__name {
    color: var(--brand-blue); font-weight: 700; font-size: 24px; line-height: 1.05;
  }
  .front-divider {
    position: absolute; left: 282px; top: 34px; width: 1px; height: 118px;
    background: var(--divider);
  }
  .contact { position: absolute; left: 300px; top: 36px; }
  .contact__name { color: var(--brand-blue); font-weight: 700; font-size: 19px; }
  .contact__title { color: var(--text-grey); font-size: 13px; margin-top: 1px; }
  .contact__list { list-style: none; margin-top: 18px; }
  .contact__item {
    display: flex; align-items: center; gap: 8px;
    color: var(--text-grey); font-size: 12.5px; margin-bottom: 6px;
  }
  .contact__icon { width: 13px; height: 13px; flex: none; }
  .front-web {
    position: absolute; right: 40px; bottom: 26px;
    color: var(--card-white); font-size: 14px; letter-spacing: 2px;
  }

  /* Back */
  .card--back { background: var(--brand-blue); }
  .services {
    position: absolute; left: 44px; top: 70px; list-style: none;
  }
  .services__item {
    color: var(--card-white); font-size: 26px; line-height: 1.6;
    text-transform: uppercase; display: flex; align-items: center; gap: 12px;
  }
  .services__item::before {
    content: ""; width: 6px; height: 6px; border-radius: 50%;
    background: var(--card-white);
  }
  .back-brand {
    position: absolute; right: 40px; top: 80px; width: 190px;
    display: flex; flex-direction: column; align-items: center; gap: 14px;
  }
  .back-brand__mark {
    width: 70px; height: 70px; border-radius: 50%; background: var(--card-white);
  }
  .back-brand__name {
    color: var(--card-white); font-weight: 700; font-size: 28px;
    text-align: center; line-height: 1.1;
  }
</style>
</head>
<body>
<main class="stage">
  <section class="card card--front" aria-label="Card front">
    <svg class="front-band" viewBox="0 0 540 310" preserveAspectRatio="none" aria-hidden="true">
      <path d="M0 190 Q 260 300 540 228 L540 310 L0 310 Z" fill="var(--brand-blue)"/>
    </svg>
    <div class="front-brand">
      <span class="front-brand__mark"></span>
      <span class="front-brand__name">Braviotrax<br>Group</span>
    </div>
    <div class="front-divider"></div>
    <div class="contact">
      <p class="contact__name">Dale Fenwick</p>
      <p class="contact__title">Managing Director</p>
      <ul class="contact__list">
        <li class="contact__item">
          <svg class="contact__icon" viewBox="0 0 16 16" aria-hidden="true">
            <circle cx="8" cy="8" r="8" fill="var(--brand-blue)"/>
            <path d="M5 4.5c.6-.4 1.2-.2 1.5.4l.5 1c.2.4 0 .8-.3 1l-.4.3c.4.9 1 1.6 1.9 2l.3-.4c.3-.3.7-.4 1-.2l1 .5c.6.3.7 1 .3 1.5-.8.9-2 1-3.2.3C6.2 10 5 8.6 4.5 7 4.2 6 4.4 5 5 4.5z" fill="#fff"/>
          </svg>
          0412 557 208
        </li>
        <li class="contact__item">
          <svg class="contact__icon" viewBox="0 0 16 16" aria-hidden="true">
            <circle cx="8" cy="8" r="8" fill="var(--brand-blue)"/>
            <rect x="4" y="5" width="8" height="6" fill="#fff"/>
            <path d="M4 5 L8 8.5 L12 5" fill="none" stroke="var(--brand-blue)" stroke-width="1"/>
          </svg>
          Dale@braviotraxgroup.com
        </li>
      </ul>
    </div>
    <p class="front-web">www.braviotraxgroup.com</p>
  </section>

  <section class="card card--back" aria-label="Card back">
    <ul class="services">
      <li class="services__item">Alliances</li>
      <li class="services__item">Placement</li>
      <li class="services__item">Training</li>
      <li class="services__item">Support</li>
    </ul>
    <div class="back-brand">
      <span class="back-brand__mark"></span>
      <span class="back-brand__name">Braviotrax<br>Group</span>
    </div>
  </section>
</main>
</body>
</html>
```